New Business Tri Fold Brochure

Tri Fold Brochure for new business. I have attached a few versions of our logo and would like the color scheme to be the blue and grey colors from the logo. I have also attached examples of the data that I would like implemented into the brochure such as the FAQ's and general company information. I would like the 3 general points (hassle free, save money, no risk guarantee) to be matched to appropriate icons. I also need the 3 steps for "how it works" matched to appropriate themed icons. I would like the back of the brochure to have a photo of our building, map of location and all contact information. Address: 728 W. Brindle Crest Ave Suite 410 Fort Lauderdale FL 33417. Phone- 754-618-2094. Email: info@harbor-tallyworks.com. Website: www.harbor-tallyworks.com

```html
<!DOCTYPE html>
<html lang="en">
<head>
<meta charset="utf-8">
<title>Harbor Tallyworks – Tri Fold Brochure</title>
<link href="https://fonts.googleapis.com/css2?family=Open+Sans:wght@400;600;700;800&family=Oswald:wght@400;500;600&display=swap" rel="stylesheet">
<style>
  :root{
    --blue:#1f5fb0;
    --blue-dark:#143f7e;
    --blue-light:#2f86d6;
    --grey:#6b6e72;
    --grey-dark:#45484c;
    --grey-light:#f2f3f5;
    --grey-mid:#c9ccd1;
    --white:#ffffff;
    --stage:#e4e5e7;
  }
  *{box-sizing:border-box;margin:0;padding:0}
  html,body{width:1200px;height:2400px;overflow:hidden}
  body{background:var(--stage);font-family:"Open Sans",Arial,sans-serif;color:var(--grey-dark);position:relative}

  .spread{position:absolute;left:51px;width:1098px;height:850px;display:flex;box-shadow:0 10px 30px rgba(0,0,0,.18);background:var(--white)}
  .spread--outside{top:230px}
  .spread--inside{top:1320px}
  .panel{position:relative;width:366px;height:850px;overflow:hidden}
  .panel + .panel{border-left:1px solid rgba(0,0,0,.06)}
  .abs{position:absolute}
  .photo{position:absolute;left:0;width:100%}

  /* brand name */
  .brand{position:absolute;left:0;width:100%;display:flex;align-items:center;justify-content:center;gap:10px}
  .brand__dot{width:34px;height:34px;border-radius:50%;background:var(--blue)}
  .brand__name{font-family:"Open Sans",Arial,sans-serif;font-weight:800;color:var(--blue);font-size:22px;line-height:1.05;letter-spacing:.5px;text-transform:uppercase}

  .pill{position:absolute;left:50%;transform:translateX(-50%);border-radius:20px;text-align:center;font-weight:700}
  .pill--site{width:270px;height:30px;line-height:30px;background:var(--grey-mid);color:var(--white);font-size:13px}
  .pill--contact{width:240px;height:32px;line-height:32px;background:var(--blue);color:var(--white);font-size:13px;letter-spacing:1px}

  .icon-ring{width:48px;height:48px;border-radius:50%;border:2px solid var(--white);background:var(--blue-light);display:flex;align-items:center;justify-content:center;flex:none}
  .icon-ring svg{width:26px;height:26px}

  /* FAQ */
  .faq{background:var(--grey-light)}
  .faq__title{position:absolute;top:34px;left:30px;right:30px;display:flex;align-items:center;gap:10px;font-family:"Oswald",sans-serif;font-size:26px;color:var(--blue)}
  .faq__title::before{content:"";flex:1;height:2px;background:var(--blue)}
  .faq__list{position:absolute;top:92px;left:30px;right:28px}
  .faq__item{margin-bottom:16px}
  .faq__q{display:flex;align-items:center;gap:8px;font-weight:700;font-size:13px;color:var(--blue);margin-bottom:5px}
  .faq__q span.dot{width:20px;height:20px;border-radius:50%;background:var(--blue);color:var(--white);font-size:12px;text-align:center;line-height:20px;flex:none}
  .faq__a{font-size:10.5px;line-height:1.5;color:var(--grey)}

  /* back */
  .contact__lines{position:absolute;top:392px;left:0;width:100%;text-align:center;font-size:13px;line-height:1.55;color:var(--grey-dark)}
  .contact__phone{display:flex;justify-content:center;align-items:center;gap:6px;font-weight:700;margin-bottom:6px}
  .contact__phone svg{width:14px;height:14px}
  .contact__gap{height:8px}
  .map{position:absolute;top:548px;left:103px;width:160px;height:160px;border-radius:50%;border:4px solid var(--white);box-shadow:0 2px 8px rgba(0,0,0,.15);background:linear-gradient(135deg,#e8e4d8,#cfdbe6)}
  .site-band{position:absolute;bottom:0;left:0;width:100%;height:60px;text-align:center;line-height:60px;color:var(--white);font-size:15px}
  .site-band b{font-weight:700}

  /* cover */
  .badges{position:absolute;left:0;width:100%;display:flex;justify-content:space-around;padding:0 30px}
  .badge{display:flex;flex-direction:column;align-items:center;gap:6px;color:var(--white);font-size:8.5px;font-weight:700;letter-spacing:.4px;text-transform:uppercase}
  .headline{position:absolute;left:0;width:100%;text-align:center;font-family:"Oswald",sans-serif;font-weight:500;color:var(--white);font-size:29px;letter-spacing:.3px}

  /* inside left */
  .points{position:absolute;top:440px;left:26px;right:24px}
  .point{display:flex;gap:14px;margin-bottom:26px;color:var(--white)}
  .point h3{font-size:14px;font-weight:800;letter-spacing:.4px;margin-bottom:3px}
  .point p{font-size:11.5px;line-height:1.45;color:#dbe7f6}
  .contact-title{position:absolute;left:0;width:100%;text-align:center;color:var(--white);font-weight:800;font-size:15px;letter-spacing:1px}

  /* inside middle */
  .team-photo{position:absolute;top:110px;left:83px;width:200px;height:200px;border-radius:50%;border:5px solid var(--blue);background:linear-gradient(160deg,#cdb9a4,#7a6a5e)}
  .section-title{position:absolute;left:0;width:100%;text-align:center;font-weight:800;color:var(--blue);font-size:17px;letter-spacing:.6px}
  .body-copy{position:absolute;left:30px;right:30px;font-size:11.5px;line-height:1.55;color:var(--grey);text-align:center}
  .body-copy p + p{margin-top:10px}

  /* inside right */
  .how__title{position:absolute;top:40px;left:0;width:100%;text-align:center;font-family:"Oswald",sans-serif;font-size:26px;color:var(--white);letter-spacing:.4px}
  .steps{position:absolute;top:110px;left:26px;right:26px}
  .step{display:flex;gap:14px;margin-bottom:34px;color:var(--white)}
  .step h3{font-size:14px;font-weight:800;letter-spacing:.4px;margin-bottom:4px}
  .step p{font-size:11.5px;line-height:1.5;color:#dbe7f6}
</style>
</head>
<body>

<!-- OUTSIDE -->
<section class="spread spread--outside">

  <!-- FAQ panel -->
  <article class="panel faq">
    <h2 class="faq__title">FAQ</h2>
    <div class="faq__list">
      <div class="faq__item">
        <div class="faq__q"><span class="dot">?</span>How does it work?</div>
        <p class="faq__a">Once you sign up, we review your current statements and negotiate directly with your provider to lower your processing rates. You keep your provider, your equipment and your routine.</p>
      </div>
      <div class="faq__item">
        <div class="faq__q"><span class="dot">?</span>How will I receive my savings?</div>
        <p class="faq__a">Your savings appear as lower fees on your monthly statement. There are no checks to wait for; the money simply stays in your account each month.</p>
      </div>
      <div class="faq__item">
        <div class="faq__q"><span class="dot">?</span>Will you switch my service provider without asking?</div>
        <p class="faq__a">Never. We work with your current provider and nothing changes without your written approval. You stay in full control of every decision we make.</p>
      </div>
      <div class="faq__item">
        <div class="faq__q"><span class="dot">?</span>How much does Harbor Tallyworks cost?</div>
        <p class="faq__a">Our fee is a share of the savings we secure for you. If we do not lower your bill, you owe us nothing at all for our time or service.</p>
      </div>
      <div class="faq__item">
        <div class="faq__q"><span class="dot">?</span>Are there any risks involved?</div>
        <p class="faq__a">No. With our No Risk Guarantee you either save money or pay nothing. It is that simple.</p>
      </div>
    </div>
    <svg class="abs" style="left:0;bottom:0" width="366" height="130" viewBox="0 0 366 130" aria-hidden="true">
      <path d="M0 40 C120 0 240 90 366 30 L366 130 L0 130Z" fill="var(--blue-light)" opacity=".55"/>
      <path d="M0 70 C130 30 250 110 366 60 L366 130 L0 130Z" fill="var(--blue)"/>
    </svg>
  </article>

  <!-- Back panel -->
  <article class="panel back">
    <div class="photo" style="top:0;height:250px;background:linear-gradient(180deg,#b9d3ea 0%,#8fa8b8 55%,#5e6f63 100%)" role="img" aria-label="Photo of the company office building"></div>
    <svg class="abs" style="left:0;top:200px" width="366" height="60" viewBox="0 0 366 60" aria-hidden="true">
      <path d="M0 30 C120 60 250 0 366 25 L366 60 L0 60Z" fill="var(--white)"/>
    </svg>
    <div class="brand" style="top:268px"><span class="brand__dot"></span><span class="brand__name">Harbor<br>Tallyworks</span></div>
    <div class="pill pill--contact" style="top:340px">CONTACT US TODAY</div>
    <div class="contact__lines">
      <div class="contact__phone">
        <svg viewBox="0 0 24 24" aria-hidden="true"><path d="M6.6 10.8a15 15 0 0 0 6.6 6.6l2.2-2.2a1 1 0 0 1 1-.25 11.4 11.4 0 0 0 3.6.57 1 1 0 0 1 1 1V20a1 1 0 0 1-1 1A17 17 0 0 1 3 4a1 1 0 0 1 1-1h3.5a1 1 0 0 1 1 1c0 1.25.2 2.45.57 3.6a1 1 0 0 1-.25 1Z" fill="var(--blue)"/></svg>
        754-618-2094
      </div>
      728 W. Brindle Crest Ave Suite 410<br>
      Fort Lauderdale FL 33417
      <div class="contact__gap"></div>
      info@harbor-tallyworks.com<br>
      www.harbor-tallyworks.com
    </div>
    <div class="map" role="img" aria-label="Map showing the office location"></div>
    <svg class="abs" style="left:0;bottom:0" width="366" height="110" viewBox="0 0 366 110" aria-hidden="true">
      <path d="M0 30 C130 0 240 60 366 20 L366 110 L0 110Z" fill="var(--blue-light)" opacity=".5"/>
      <path d="M0 50 C130 25 240 75 366 45 L366 110 L0 110Z" fill="var(--blue)"/>
    </svg>
    <div class="site-band">www.<b>harbor-tallyworks</b>.com</div>
  </article>

  <!-- Cover panel -->
  <article class="panel cover">
    <div class="brand" style="top:60px"><span class="brand__dot"></span><span class="brand__name">Harbor<br>Tallyworks</span></div>
    <div class="photo" style="top:170px;height:430px;background:linear-gradient(160deg,#d9d2c6 0%,#9c8a78 50%,#4f4a48 100%)" role="img" aria-label="Photo of a smiling business owner holding a tablet in her shop"></div>
    <svg class="abs" style="left:0;top:140px" width="366" height="70" viewBox="0 0 366 70" aria-hidden="true">
      <path d="M0 0 L366 0 L366 20 C250 60 120 20 0 50Z" fill="var(--white)"/>
      <path d="M0 50 C120 20 250 60 366 20" fill="none" stroke="var(--grey)" stroke-width="6"/>
      <path d="M0 56 C120 28 250 68 366 28" fill="none" stroke="var(--blue)" stroke-width="3"/>
    </svg>
    <svg class="abs" style="left:0;top:540px" width="366" height="310" viewBox="0 0 366 310" aria-hidden="true">
      <path d="M0 40 C120 0 250 70 366 20 L366 310 L0 310Z" fill="var(--blue-light)" opacity=".6"/>
      <path d="M0 60 C120 25 250 90 366 45 L366 310 L0 310Z" fill="var(--blue)"/>
      <path d="M0 180 L366 150 L366 310 L0 310Z" fill="var(--blue-dark)" opacity=".55"/>
    </svg>
    <div class="badges" style="top:610px">
      <div class="badge"><span class="icon-ring"><svg viewBox="0 0 24 24" aria-hidden="true"><path d="M12 2 4 5v6c0 5 3.4 9.4 8 11 4.6-1.6 8-6 8-11V5Z" fill="none" stroke="#fff" stroke-width="2"/><path d="m8.5 12 2.5 2.5 4.5-5" fill="none" stroke="#fff" stroke-width="2"/></svg></span>Hassle free</div>
      <div class="badge"><span class="icon-ring"><svg viewBox="0 0 24 24" aria-hidden="true"><circle cx="12" cy="12" r="9" fill="none" stroke="#fff" stroke-width="2"/><path d="M15 9c-.5-1-1.6-1.5-3-1.5-1.7 0-3 .8-3 2s1.3 1.7 3 2 3 .8 3 2-1.3 2-3 2c-1.4 0-2.5-.5-3-1.5M12 6v12" fill="none" stroke="#fff" stroke-width="1.8"/></svg></span>Save money</div>
      <div class="badge"><span class="icon-ring"><svg viewBox="0 0 24 24" aria-hidden="true"><path d="m5 12.5 4.5 4.5L19 7.5" fill="none" stroke="#fff" stroke-width="2.6"/></svg></span>No risk guarantee</div>
    </div>
    <h1 class="headline" style="top:712px">SAVE YOUR BUSINESS MONEY!</h1>
    <div class="pill pill--site" style="top:776px">www.<b>harbor-tallyworks</b>.com</div>
  </article>
</section>

<!-- INSIDE -->
<section class="spread spread--inside">

  <!-- Benefits panel -->
  <article class="panel benefits">
    <div class="photo" style="top:0;height:420px;background:linear-gradient(160deg,#e6e1da 0%,#a9a097 55%,#5d5955 100%)" role="img" aria-label="Photo of a customer handing a payment card across a shop counter"></div>
    <svg class="abs" style="left:0;top:360px" width="366" height="490" viewBox="0 0 366 490" aria-hidden="true">
      <path d="M0 30 C130 70 250 0 366 20 L366 490 L0 490Z" fill="var(--blue-light)" opacity=".6"/>
      <path d="M0 50 C130 90 250 20 366 42 L366 490 L0 490Z" fill="var(--blue)"/>
    </svg>
    <div class="points">
      <div class="point"><span class="icon-ring"><svg viewBox="0 0 24 24" aria-hidden="true"><path d="M12 2 4 5v6c0 5 3.4 9.4 8 11 4.6-1.6 8-6 8-11V5Z" fill="none" stroke="#fff" stroke-width="2"/><path d="m8.5 12 2.5 2.5 4.5-5" fill="none" stroke="#fff" stroke-width="2"/></svg></span>
        <div><h3>HASSLE FREE</h3><p>You're busy running a business; let us negotiate for you and put money back in your pocket!</p></div></div>
      <div class="point"><span class="icon-ring"><svg viewBox="0 0 24 24" aria-hidden="true"><circle cx="12" cy="12" r="9" fill="none" stroke="#fff" stroke-width="2"/><path d="M15 9c-.5-1-1.6-1.5-3-1.5-1.7 0-3 .8-3 2s1.3 1.7 3 2 3 .8 3 2-1.3 2-3 2c-1.4 0-2.5-.5-3-1.5M12 6v12" fill="none" stroke="#fff" stroke-width="1.8"/></svg></span>
        <div><h3>SAVE MONEY</h3><p>We save business owners an average of $500 per month.</p></div></div>
      <div class="point"><span class="icon-ring"><svg viewBox="0 0 24 24" aria-hidden="true"><path d="m5 12.5 4.5 4.5L19 7.5" fill="none" stroke="#fff" stroke-width="2.6"/></svg></span>
        <div><h3>NO RISK GUARANTEE</h3><p>We guarantee we will lower your bill or there is no charge for our service!</p></div></div>
    </div>
    <div class="contact-title" style="top:752px">CONTACT US TODAY</div>
    <div class="pill pill--site" style="top:788px">www.<b>harbor-tallyworks</b>.com</div>
  </article>

  <!-- About panel -->
  <article class="panel about">
    <div class="brand" style="top:38px"><span class="brand__dot"></span><span class="brand__name">Harbor<br>Tallyworks</span></div>
    <div class="team-photo" role="img" aria-label="Photo of two shop staff in aprons reviewing a tablet"></div>
    <h2 class="section-title" style="top:336px">WHO WE ARE</h2>
    <div class="body-copy" style="top:366px">
      <p>Harbor Tallyworks is a company that was founded by proven merchant processing professionals with over 20 years of industry knowledge and experience.</p>
      <p>We know all of the tricks that the big companies use to fill their pockets with your money. We use that knowledge to negotiate and save your business money.</p>
    </div>
    <h2 class="section-title" style="top:560px">WHAT WE DO</h2>
    <div class="body-copy" style="top:590px">
      <p>Once you sign up, our experts get to work negotiating with your current merchant processing provider. Our goal is to get you the lowest rates possible without changing providers or buying new equipment.</p>
      <p>We offer a No Risk Savings Guarantee. If we can't save you money, you don't pay us a dime. 100% risk free.</p>
    </div>
    <svg class="abs" style="left:0;bottom:0" width="366" height="40" viewBox="0 0 366 40" aria-hidden="true">
      <path d="M0 25 C130 5 240 35 366 15 L366 40 L0 40Z" fill="var(--blue)"/>
    </svg>
  </article>

  <!-- How it works panel -->
  <article class="panel how">
    <div class="abs" style="left:0;top:0;width:366px;height:620px;background:var(--blue)"></div>
    <h2 class="how__title">HOW IT WORKS?</h2>
    <div class="steps">
      <div class="step"><span class="icon-ring"><svg viewBox="0 0 24 24" aria-hidden="true"><path d="M4 20h4L19 9l-4-4L4 16Z" fill="none" stroke="#fff" stroke-width="2"/><path d="m13.5 6.5 4 4" stroke="#fff" stroke-width="2"/></svg></span>
        <div><h3>SIGN UP</h3><p>Provide some basic information and a copy of your most recent statement or invoice.</p></div></div>
      <div class="step"><span class="icon-ring"><svg viewBox="0 0 24 24" aria-hidden="true"><path d="M6.6 10.8a15 15 0 0 0 6.6 6.6l2.2-2.2a1 1 0 0 1 1-.25 11.4 11.4 0 0 0 3.6.57 1 1 0 0 1 1 1V20a1 1 0 0 1-1 1A17 17 0 0 1 3 4a1 1 0 0 1 1-1h3.5a1 1 0 0 1 1 1c0 1.25.2 2.45.57 3.6a1 1 0 0 1-.25 1Z" fill="#fff"/></svg></span>
        <div><h3>WE CONTACT YOUR PROVIDER</h3><p>Our experts get to work negotiating with your current provider on your behalf for the lowest rates possible.</p></div></div>
      <div class="step"><span class="icon-ring"><svg viewBox="0 0 24 24" aria-hidden="true"><rect x="3" y="6" width="18" height="12" rx="2" fill="none" stroke="#fff" stroke-width="2"/><circle cx="12" cy="12" r="3" fill="none" stroke="#fff" stroke-width="2"/></svg></span>
        <div><h3>YOU SAVE MONEY</h3><p>Your monthly fees get reduced and the money we save you goes straight back into your wallet. Simple!</p></div></div>
    </div>
    <div class="photo" style="top:560px;height:290px;background:linear-gradient(160deg,#e9e4dc 0%,#b7a896 50%,#6f8a5c 100%)" role="img" aria-label="Photo of a business owner reviewing paperwork at her desk"></div>
    <svg class="abs" style="left:0;top:540px" width="366" height="70" viewBox="0 0 366 70" aria-hidden="true">
      <path d="M0 0 L366 0 L366 30 C250 60 120 10 0 45Z" fill="var(--blue)"/>
      <path d="M0 45 C120 10 250 60 366 30" fill="none" stroke="var(--white)" stroke-width="4"/>
    </svg>
  </article>
</section>

</body>
</html>
```